Apartments rental business needs a web for direct reservations.

I need a website that allows my clients to check the property (pictures, a brief description etc) and lets them make reservations. They will be providing the required information such as name, last name, email address and credit card details. Also a calendar where I can update the availability (dates and prices) of the property upon new reservations is a must. I already have a logo that should also be a good starting point for colors, style an inspiration.

Need extra days to review

```html
<!DOCTYPE html>
<html lang="en">
<head>
<meta charset="utf-8">
<title>Orchard Bay Bungalows</title>
<link href="https://fonts.googleapis.com/css2?family=Open+Sans:ital,wght@0,300;0,400;0,600;0,700;1,400&display=swap" rel="stylesheet">
<style>
:root{
  --orange:#f39a2c;
  --teal:#1b877a;
  --teal-light:#2bb3a3;
  --ink:#222222;
  --text:#555555;
  --muted:#9a9a9a;
  --paper:#ffffff;
  --soft:#f5f4f4;
  --card:#f1f1f1;
  --footer:#232323;
  --footer-bottom:#1a1a1a;
  --field:#2c2c2c;
}
*{margin:0;padding:0;box-sizing:border-box}
html,body{width:1200px;height:2807px;overflow:hidden}
body{font-family:"Open Sans",Arial,sans-serif;color:var(--text);background:var(--paper);position:relative}
.abs{position:absolute}

/* hero */
.hero{position:absolute;left:0;top:0;width:1200px;height:573px;
  background:linear-gradient(180deg,#b9c7cf 0%,#7f9a86 30%,#4d6b4a 52%,#3aa0c4 68%,#5fb6d0 80%,#8a6b55 100%)}
.nav-band{position:absolute;left:0;top:0;width:1200px;height:122px;background:rgba(255,255,255,.85)}
.nav a{position:absolute;top:44px;font-size:12.5px;font-weight:600;color:#333;text-decoration:none;letter-spacing:.3px}
.nav a.active{color:var(--orange)}
.brand{position:absolute;left:520px;top:14px;width:200px;text-align:center;color:var(--orange);font-weight:700}
.brand-dot{width:34px;height:34px;border-radius:50%;background:var(--orange);margin:0 auto 6px}
.brand-name{font-size:17px;line-height:20px;letter-spacing:.5px;white-space:nowrap}
.brand-sub{font-size:8px;letter-spacing:1.5px;line-height:12px}
.hero-title{position:absolute;left:0;top:196px;width:1200px;text-align:center;color:#fff;font-weight:300;font-size:46px;line-height:64px;text-shadow:0 2px 6px rgba(0,0,0,.3)}
.slide-arrow{position:absolute;top:322px;width:47px;height:50px;background:rgba(255,255,255,.85);display:flex;align-items:center;justify-content:center}

/* booking */
.booking{position:absolute;left:159px;top:533px;width:880px;height:92px;background:var(--teal);padding:7px}
.booking-inner{border:2px solid #fff;height:100%;position:relative}
.field{position:absolute;top:22px;width:150px;height:32px;background:#fff;font-size:12px;font-style:italic;color:#777;padding:8px 10px;display:flex;justify-content:space-between;align-items:center}
.btn-check{position:absolute;top:22px;left:690px;width:150px;height:32px;background:var(--orange);color:#fff;font-size:11px;font-weight:700;display:flex;align-items:center;justify-content:center}

/* welcome */
.welcome{position:absolute;left:0;top:573px;width:1200px;height:655px;background:var(--soft)}
.welcome-kicker{position:absolute;left:171px;top:108px;font-size:25px;color:var(--ink)}
.welcome-kicker span{color:var(--orange)}
.welcome-title{position:absolute;left:171px;top:140px;font-size:32px;font-weight:700;color:var(--ink);line-height:44px;letter-spacing:.5px}
.title-rule{position:absolute;left:366px;top:205px;width:88px;height:2px;background:var(--orange)}
.welcome-text{position:absolute;left:171px;top:248px;width:420px;font-size:12.5px;line-height:19px}
.welcome-text p{margin-bottom:12px}
.btn{position:absolute;height:33px;font-size:12px;font-weight:700;color:#fff;display:flex;align-items:center;justify-content:center;letter-spacing:.3px}
.btn-orange{background:var(--orange)}
.btn-dark{background:#2b2b2b}
.photo{position:absolute}
.amenity{position:absolute;top:473px;width:94px;height:128px;background:#fff;box-shadow:0 1px 5px rgba(0,0,0,.15);text-align:center;font-size:12px;color:#333;line-height:15px}
.amenity svg{display:block;margin:20px auto 12px}

/* rooms */
.rooms{position:absolute;left:0;top:1228px;width:1200px;height:662px;background:var(--teal)}
.thumb{position:absolute;top:440px;width:104px;height:89px}
.sq-arrow{position:absolute;top:554px;width:33px;height:33px;background:#e7f4f2;display:flex;align-items:center;justify-content:center}
.rooms-kicker{position:absolute;left:625px;top:74px;font-size:26px;color:#fff;font-weight:400}
.rooms-title{position:absolute;left:625px;top:106px;font-size:34px;font-weight:700;color:#fff;line-height:44px}
.rooms-text{position:absolute;left:625px;top:203px;width:400px;font-size:13px;line-height:20px;color:#eaf6f4}
.features{position:absolute;left:655px;top:304px;width:332px;height:234px;display:grid;grid-template-columns:repeat(3,1fr);grid-template-rows:repeat(3,1fr)}
.feature{color:#fff;font-size:13px;text-align:center;display:flex;flex-direction:column;align-items:center;justify-content:center;gap:8px;border-color:rgba(255,255,255,.6);border-style:dashed;border-width:0}
.feature.r{border-right-width:1px}
.feature.b{border-bottom-width:1px}

/* testimonials */
.testimonials{position:absolute;left:0;top:1890px;width:1200px;height:449px;background:#fff}
.t-title{position:absolute;left:154px;top:58px;font-size:30px;font-weight:400;color:var(--ink)}
.t-sub{position:absolute;left:154px;top:98px;font-size:11px;font-style:italic;color:#b5b5b5}
.t-rule{position:absolute;left:518px;top:107px;width:95px;height:2px;background:var(--orange)}
.quote{position:absolute;top:136px;height:138px;background:var(--card);padding:28px 30px;font-size:12.5px;line-height:20px;color:#555}
.quote::after{content:"";position:absolute;left:40px;bottom:-18px;border-left:18px solid transparent;border-right:0 solid transparent;border-top:18px solid var(--card)}
.avatar{position:absolute;top:299px;width:80px;height:80px;border-radius:50%;background:linear-gradient(160deg,#e9dfd5,#b7a594);border:3px solid #fff;box-shadow:0 1px 4px rgba(0,0,0,.2)}
.person{position:absolute;top:318px;font-size:14px;color:#333}
.person small{font-size:11px;color:#777}
.stars{position:absolute;top:342px;color:var(--orange);font-size:12px;letter-spacing:2px}

/* footer */
.footer{position:absolute;left:0;top:2339px;width:1200px;height:433px;background:var(--footer);color:#ddd}
.f-head{position:absolute;top:50px;font-size:20px;font-weight:700;color:#fff}
.f-rule{position:absolute;top:82px;width:44px;height:2px;background:var(--orange)}
.f-text{position:absolute;font-size:12.5px;line-height:21px;color:#ddd}
.f-input{position:absolute;background:var(--field);border:1px solid #333;font-size:12px;color:#bbb;padding:10px 14px}
.socials{position:absolute;left:194px;top:310px;display:flex;gap:18px}
.socials span{width:12px;height:12px;border-radius:50%;background:#ddd;display:block}
.copyright{position:absolute;left:0;top:2772px;width:1200px;height:35px;background:var(--footer-bottom);font-size:11px;color:#8a8a8a;padding:10px 187px}
</style>
</head>
<body>

<section class="hero" role="img" aria-label="Photo of the bungalow complex pool with palm trees, parasols and sun loungers">
  <div class="nav-band"></div>
  <nav class="nav">
    <a class="active" style="left:300px">HOME</a>
    <a style="left:364px">ABOUT US</a>
    <a style="left:452px">ROOMS</a>
    <a style="left:703px">PACKAGES</a>
    <a style="left:790px">GALLERY</a>
    <a style="left:868px">CONTACT US</a>
    <svg style="position:absolute;left:988px;top:44px" width="16" height="16" viewBox="0 0 16 16"><circle cx="6.5" cy="6.5" r="5" fill="none" stroke="#333" stroke-width="2"/><line x1="10" y1="10" x2="15" y2="15" stroke="#333" stroke-width="2"/></svg>
  </nav>
  <div class="brand">
    <div class="brand-dot"></div>
    <div class="brand-name">ORCHARD BAY</div>
    <div class="brand-sub">BUNGALOWS</div>
  </div>
  <h1 class="hero-title">Your best memories start here ...<br>at Orchard Bay Bungalows</h1>
  <div class="slide-arrow" style="left:42px"><svg width="14" height="20" viewBox="0 0 14 20"><polyline points="11,2 3,10 11,18" fill="none" stroke="#333" stroke-width="3"/></svg></div>
  <div class="slide-arrow" style="left:1111px"><svg width="14" height="20" viewBox="0 0 14 20"><polyline points="3,2 11,10 3,18" fill="none" stroke="#333" stroke-width="3"/></svg></div>
</section>

<section class="welcome">
  <div class="welcome-kicker">Welcome to <span>Orchard Bay</span></div>
  <h2 class="welcome-title">Bungalows For Your<br>Dream Stay</h2>
  <div class="title-rule"></div>
  <div class="welcome-text">
    <p>Orchard Bay Bungalows 45 &amp; 46 apartment features accommodation with complimentary parking, a golf course and a safe deposit box.</p>
    <p>All units have free WiFi, a mini bar, heating, cable TV with on-demand movies and a private safe. The apartment holds 2 bedrooms.</p>
  </div>
  <div class="btn btn-orange" style="left:173px;top:365px;width:136px">READ MORE</div>
  <div class="btn btn-dark" style="left:318px;top:365px;width:136px">SHOW ON MAP</div>
  <div class="photo" style="left:613px;top:89px;width:412px;height:334px;background:linear-gradient(180deg,#e6e8e6 0%,#d9dcdb 55%,#6d6f73 70%,#a63a3a 78%,#8a8278 100%)" role="img" aria-label="Photo of the apartment living room with grey sofa, red cushions and framed line art"></div>

  <div class="amenity" style="left:171px"><svg width="46" height="46" viewBox="0 0 46 46" fill="none" stroke="#f39a2c" stroke-width="2.5"><path d="M5 18a26 26 0 0 1 36 0"/><path d="M11 25a17 17 0 0 1 24 0"/><path d="M17 32a8 8 0 0 1 12 0"/><circle cx="23" cy="38" r="2" fill="#f39a2c"/></svg>Free Wi-Fi</div>
  <div class="amenity" style="left:281px"><svg width="46" height="46" viewBox="0 0 46 46" fill="none" stroke="#f39a2c" stroke-width="2.5"><path d="M6 30l4-12h22l4 12v8H6z"/><circle cx="13" cy="32" r="2"/><circle cx="29" cy="32" r="2"/><rect x="32" y="4" width="10" height="10"/><line x1="37" y1="14" x2="37" y2="22"/></svg>Free Parking</div>
  <div class="amenity" style="left:391px"><svg width="46" height="46" viewBox="0 0 46 46" fill="none" stroke="#f39a2c" stroke-width="2.5"><path d="M14 32V8a4 4 0 0 1 8 0M28 32V8a4 4 0 0 1 8 0"/><line x1="14" y1="16" x2="28" y2="16"/><line x1="14" y1="24" x2="28" y2="24"/><path d="M4 36q5-4 10 0t10 0 10 0 10 0"/><path d="M4 42q5-4 10 0t10 0 10 0 10 0"/></svg>Swimming<br>Pool</div>
  <div class="amenity" style="left:501px"><svg width="46" height="46" viewBox="0 0 46 46" fill="none" stroke="#f39a2c" stroke-width="2.5"><circle cx="16" cy="16" r="10"/><line x1="23" y1="23" x2="40" y2="40"/><circle cx="34" cy="10" r="4"/></svg>Sports<br>Activities</div>
  <div class="amenity" style="left:611px"><svg width="46" height="46" viewBox="0 0 46 46" fill="none" stroke="#f39a2c" stroke-width="2.5"><rect x="6" y="24" width="34" height="7"/><line x1="33" y1="24" x2="33" y2="31"/><line x1="6" y1="8" x2="40" y2="40"/></svg>Non<br>Smoking</div>
  <div class="amenity" style="left:721px"><svg width="46" height="46" viewBox="0 0 46 46" fill="none" stroke="#f39a2c" stroke-width="2.5"><circle cx="23" cy="24" r="16"/><circle cx="17" cy="22" r="1.5" fill="#f39a2c"/><circle cx="29" cy="22" r="1.5" fill="#f39a2c"/><path d="M17 30q6 5 12 0"/></svg>Child<br>Friendly</div>
  <div class="amenity" style="left:831px"><svg width="46" height="46" viewBox="0 0 46 46" fill="none" stroke="#f39a2c" stroke-width="2.5"><path d="M6 16L23 6l17 10z"/><line x1="10" y1="16" x2="10" y2="40"/><line x1="36" y1="16" x2="36" y2="40"/><rect x="16" y="26" width="14" height="4"/><line x1="18" y1="30" x2="18" y2="40"/><line x1="28" y1="30" x2="28" y2="40"/></svg>Terrace</div>
  <div class="amenity" style="left:941px"><svg width="46" height="46" viewBox="0 0 46 46" fill="none" stroke="#f39a2c" stroke-width="2.5"><rect x="4" y="10" width="38" height="16" rx="2"/><line x1="9" y1="21" x2="37" y2="21"/><path d="M14 32v6M23 32v8M32 32v6"/></svg>Air<br>Conditioning</div>
</section>

<div class="booking">
  <div class="booking-inner">
    <div class="field" style="left:20px">Arrival Date <span>&#9638;</span></div>
    <div class="field" style="left:188px">Departure Date <span>&#9638;</span></div>
    <div class="field" style="left:356px">Adults <span>&#9662;</span></div>
    <div class="field" style="left:524px">Children <span>&#9662;</span></div>
    <div class="btn-check">CHECK AVAILABILITY</div>
  </div>
</div>

<section class="rooms">
  <div class="photo" style="left:159px;top:79px;width:440px;height:344px;background:linear-gradient(180deg,#dcdcdc 0%,#cfcfcf 45%,#2c3f7c 55%,#e8e8e8 68%,#bfbfbf 100%)" role="img" aria-label="Photo of a twin bedroom with blue headboards and folded towels"></div>
  <div class="thumb" style="left:159px;background:linear-gradient(#d8d8d8,#8c8c8c)" role="img" aria-label="Bedroom thumbnail"></div>
  <div class="thumb" style="left:271px;background:linear-gradient(#b33a3a,#7c2626)" role="img" aria-label="Living room thumbnail"></div>
  <div class="thumb" style="left:383px;background:linear-gradient(#e2e2e2,#a8a8a8)" role="img" aria-label="Kitchen thumbnail"></div>
  <div class="thumb" style="left:495px;background:linear-gradient(#c0502a,#7a3a22)" role="img" aria-label="Terrace thumbnail"></div>
  <div class="sq-arrow" style="left:526px"><svg width="10" height="14" viewBox="0 0 10 14"><polyline points="8,1 2,7 8,13" fill="none" stroke="#333" stroke-width="2"/></svg></div>
  <div class="sq-arrow" style="left:564px"><svg width="10" height="14" viewBox="0 0 10 14"><polyline points="2,1 8,7 2,13" fill="none" stroke="#333" stroke-width="2"/></svg></div>

  <div class="rooms-kicker">Know About Rooms</div>
  <h2 class="rooms-title">Discover what makes<br>us different</h2>
  <p class="rooms-text">Orchard Bay Bungalows are located inside a picturesque complex well known for its peaceful and quiet ambient. This single story bungalow is very comfortable and very well equipped.</p>

  <div class="features">
    <div class="feature r b"><svg width="26" height="20" viewBox="0 0 26 20" fill="none" stroke="#fff" stroke-width="1.6"><rect x="2" y="9" width="22" height="7"/><rect x="4" y="4" width="7" height="5"/><line x1="2" y1="16" x2="2" y2="19"/><line x1="24" y1="16" x2="24" y2="19"/></svg>2 Bedrooms</div>
    <div class="feature r b"><svg width="26" height="20" viewBox="0 0 26 20" fill="none" stroke="#fff" stroke-width="1.6"><path d="M4 7h14v6a5 5 0 0 1-5 5H9a5 5 0 0 1-5-5z"/><path d="M18 9h3a2 2 0 0 1 0 4h-3"/><path d="M9 1v4M13 1v4"/></svg>Coffee or Tea</div>
    <div class="feature b"><svg width="26" height="20" viewBox="0 0 26 20" fill="none" stroke="#fff" stroke-width="1.6"><rect x="3" y="3" width="20" height="14"/><path d="M7 3v14M11 3v14M15 3v14M19 3v14"/></svg>Heater</div>
    <div class="feature r b"><svg width="26" height="20" viewBox="0 0 26 20" fill="none" stroke="#fff" stroke-width="1.6"><path d="M3 15h20a6 6 0 0 0-6-8H9"/><line x1="3" y1="15" x2="3" y2="18"/></svg>Iron</div>
    <div class="feature r b"><svg width="26" height="20" viewBox="0 0 26 20" fill="none" stroke="#fff" stroke-width="1.6"><path d="M6 4a9 9 0 0 0 12 12z"/><line x1="12" y1="10" x2="19" y2="3"/><line x1="8" y1="16" x2="6" y2="19"/></svg>Cable Channels</div>
    <div class="feature b"><svg width="26" height="20" viewBox="0 0 26 20" fill="none" stroke="#fff" stroke-width="1.6"><path d="M4 4h12a4 4 0 0 1 0 8H4z"/><path d="M10 12l-2 7h4l2-7"/><line x1="20" y1="6" x2="24" y2="5"/><line x1="20" y1="10" x2="24" y2="11"/></svg>Hair Dryer</div>
    <div class="feature r"><svg width="26" height="20" viewBox="0 0 26 20" fill="none" stroke="#fff" stroke-width="1.6"><rect x="6" y="1" width="14" height="18"/><line x1="13" y1="1" x2="13" y2="19"/><line x1="11" y1="9" x2="11" y2="11"/><line x1="15" y1="9" x2="15" y2="11"/></svg>Closet</div>
    <div class="feature r"><svg width="26" height="20" viewBox="0 0 26 20" fill="none" stroke="#fff" stroke-width="1.6"><rect x="3" y="3" width="20" height="13"/><line x1="9" y1="19" x2="17" y2="19"/></svg>TV</div>
    <div class="feature"><svg width="26" height="20" viewBox="0 0 26 20" fill="none" stroke="#fff" stroke-width="1.6"><path d="M3 11h20v3a4 4 0 0 1-4 4H7a4 4 0 0 1-4-4z"/><path d="M5 11V4a2 2 0 0 1 4 0"/></svg>1 Bathroom</div>
  </div>
  <div class="btn btn-orange" style="left:753px;top:573px;width:136px;height:35px;font-size:11px">CHECK AVAILABILITY</div>
</section>

<section class="testimonials">
  <h2 class="t-title">Testimonials</h2>
  <div class="t-sub">Nemo enim ipsam voluptatem quia voluptas sit aspernatur</div>
  <div class="t-rule"></div>

  <div class="quote" style="left:173px;width:388px">Duis aute irure dolor in reprehenderit in voluptate velit esse cillum dolore eu fugiat nulla pariatur. Excepteur sint occaecat cupidatat non proident, sunt in culpa qui officia deserunt mollit anim id est laborum.</div>
  <div class="quote" style="left:610px;width:415px">Neque porro quisquam est, qui dolorem ipsum quia dolor sit amet, consectetur, adipisci velit, sed quia non numquam eius modi tempora incidunt ut labore et dolore magnam aliquam quaerat voluptatem.</div>

  <div class="avatar" style="left:147px" role="img" aria-label="Guest portrait"></div>
  <div class="person" style="left:236px">Owen <small>&nbsp;- Manager</small></div>
  <div class="stars" style="left:236px">★★★★★</div>
  <div class="avatar" style="left:580px" role="img" aria-label="Guest portrait"></div>
  <div class="person" style="left:673px">Lena Hart <small>&nbsp;- HR</small></div>
  <div class="stars" style="left:673px">★★★★★</div>
</section>

<footer class="footer">
  <div class="f-head" style="left:171px">Contact Us</div>
  <div class="f-rule" style="left:171px"></div>
  <p class="f-text" style="left:171px;top:112px;width:260px">Located in Costa Lumina, within 4.1 km of Lumina Water Park and 6 km of Playa de Santa Clara</p>
  <svg class="abs" style="left:171px;top:208px" width="12" height="16" viewBox="0 0 12 16"><path d="M6 0a6 6 0 0 1 6 6c0 4-6 10-6 10S0 10 0 6a6 6 0 0 1 6-6z" fill="#ddd"/><circle cx="6" cy="6" r="2" fill="#232323"/></svg>
  <p class="f-text" style="left:194px;top:204px;width:240px">27 Avenida de los Pinos, 35200<br>Costa Lumina, Spain</p>
  <svg class="abs" style="left:171px;top:258px" width="13" height="13" viewBox="0 0 13 13"><path d="M2 1l3 0 1 3-2 1a7 7 0 0 0 4 4l1-2 3 1v3a1 1 0 0 1-1 1A11 11 0 0 1 1 2a1 1 0 0 1 1-1z" fill="#ddd"/></svg>
  <p class="f-text" style="left:194px;top:254px">000 - 0000 - 0000</p>
  <div class="socials"><span></span><span></span><span></span><span></span></div>

  <div class="f-head" style="left:463px">Quick Contact</div>
  <div class="f-rule" style="left:463px"></div>
  <div class="f-input" style="left:463px;top:119px;width:269px;height:36px">Name...</div>
  <div class="f-input" style="left:463px;top:159px;width:269px;height:38px">Email...</div>
  <div class="f-input" style="left:463px;top:201px;width:269px;height:105px">Message...</div>
  <div class="btn btn-orange" style="left:463px;top:325px;width:269px;height:36px;font-size:12.5px">Submit</div>

  <div class="f-head" style="left:756px">Newsletter</div>
  <div class="f-rule" style="left:756px"></div>
  <p class="f-text" style="left:756px;top:116px;width:269px;font-size:12px;line-height:18px">Subscribe to our newsletter for latest updates</p>
  <div class="f-input" style="left:756px;top:161px;width:269px;height:36px">Email...</div>
  <div class="btn btn-orange" style="left:756px;top:206px;width:269px;height:33px;font-size:12.5px">Subscribe</div>
</footer>
<div class="copyright">©Copyright information here</div>

</body>
</html>
```